Torvane Facilities Business Card Design

We would now like to design business cards with the new Torvane Facilities logo

Target Market(s)

Professional

Industry/Entity Type

Professional services

Contact Information for Business Card

Employee name, title, phone number, email address, corporate office address and logo.

Font styles to use
Sans Serif

Colors
0054AA
0677BA
7BADD7
CADEEF
E8F1F8

Requirements
Must have
• My logo
Should not have
• any other pictures or images besides my logo

```html
<!DOCTYPE html>
<html lang="en">
<head>
<meta charset="utf-8">
<title>Torvane Facilities – Business Card</title>
<link rel="stylesheet" href="https://fonts.googleapis.com/css2?family=Oswald:wght@500;600&family=Montserrat:wght@400;500&display=swap">
<style>
  :root {
    --blue-deep: #0054AA;
    --blue-mid: #0677BA;
    --blue-soft: #7BADD7;
    --blue-pale: #CADEEF;
    --blue-mist: #E8F1F8;
    --card-text: #EDE4D6;
    --page-bg: #E4E7EA;
    --glass: #DCE3E9;
  }
  * { margin: 0; padding: 0; box-sizing: border-box; }
  html, body { width: 1200px; height: 969px; overflow: hidden; }
  body {
    background: var(--page-bg);
    font-family: "Montserrat", sans-serif;
    position: relative;
  }
  .business-card {
    position: absolute;
    left: 100px;
    top: 199px;
    width: 1000px;
    height: 571px;
    display: flex;
    box-shadow: 0 10px 30px rgba(0, 0, 0, 0.12);
    border: 1px solid rgba(255, 255, 255, 0.7);
  }
  .contact-panel {
    width: 457px;
    height: 100%;
    background: linear-gradient(160deg, var(--blue-mid) 0%, #1463D6 40%, var(--blue-deep) 100%);
    color: var(--card-text);
    padding: 118px 0 0 68px;
  }
  .person-name {
    font-family: "Oswald", sans-serif;
    font-weight: 500;
    font-size: 38px;
    letter-spacing: 0.5px;
    line-height: 1;
    text-transform: uppercase;
  }
  .person-title {
    font-size: 20px;
    margin-top: 8px;
  }
  .office-address {
    font-style: normal;
    font-size: 20px;
    line-height: 28px;
    margin-top: 42px;
  }
  .contact-list {
    list-style: none;
    margin-top: 22px;
  }
  .contact-list li {
    display: flex;
    align-items: center;
    font-size: 20px;
    height: 29px;
  }
  .contact-icon {
    width: 18px;
    height: 18px;
    margin-right: 14px;
    flex: none;
    fill: var(--card-text);
  }
  .brand-panel {
    flex: 1;
    height: 100%;
    background: linear-gradient(150deg, var(--blue-mist) 0%, var(--glass) 55%, #D6DDE3 100%);
    display: flex;
    align-items: center;
    justify-content: center;
  }
  .brand-name {
    font-family: "Oswald", sans-serif;
    font-weight: 600;
    font-size: 56px;
    line-height: 1.05;
    letter-spacing: 2px;
    color: var(--blue-deep);
    text-transform: uppercase;
    text-align: left;
  }
</style>
</head>
<body>
  <article class="business-card">
    <section class="contact-panel">
      <h1 class="person-name">Daniel Reyes</h1>
      <p class="person-title">President</p>
      <address class="office-address">
        1420 Harbor Ridge Road<br>
        Kenwick<br>
        Alaska 99517
      </address>
      <ul class="contact-list">
        <li>
          <svg class="contact-icon" viewBox="0 0 24 24" aria-hidden="true"><path d="M6.6 10.8a15.1 15.1 0 0 0 6.6 6.6l2.2-2.2c.3-.3.7-.4 1-.2 1.1.4 2.3.6 3.6.6.6 0 1 .4 1 1V20c0 .6-.4 1-1 1A17 17 0 0 1 3 4c0-.6.4-1 1-1h3.5c.6 0 1 .4 1 1 0 1.3.2 2.5.6 3.6.1.3 0 .7-.2 1z"/></svg>
          555-214-0736
        </li>
        <li>
          <svg class="contact-icon" viewBox="0 0 24 24" aria-hidden="true"><path d="M7 2h10a2 2 0 0 1 2 2v16a2 2 0 0 1-2 2H7a2 2 0 0 1-2-2V4a2 2 0 0 1 2-2zm0 3v13h10V5zm5 14.2a1 1 0 1 0 0 1.6 1 1 0 0 0 0-1.6z"/></svg>
          555-318-4290
        </li>
        <li>
          <svg class="contact-icon" viewBox="0 0 24 24" aria-hidden="true"><path d="M2 6h20v12H2zm2 1.5v.3l8 5 8-5v-.3z"/></svg>
          info@torvanefacilities.com
        </li>
        <li>
          <svg class="contact-icon" viewBox="0 0 24 24" aria-hidden="true"><path d="M12 2a10 10 0 1 0 0 20 10 10 0 0 0 0-20zm-1 17.9A8 8 0 0 1 4.2 10L9 14.8v1a2 2 0 0 0 2 2zm6.9-2.5a2 2 0 0 0-1.9-1.4h-1v-3a1 1 0 0 0-1-1H8v-2h2a1 1 0 0 0 1-1V7h2a2 2 0 0 0 2-2v-.4a8 8 0 0 1 2.9 12.8z"/></svg>
          www.torvanefacilities.com
        </li>
      </ul>
    </section>
    <section class="brand-panel">
      <p class="brand-name">Torvane<br>Facilities</p>
    </section>
  </article>
</body>
</html>
```